Velquor Web Site

We need a new web site for a new company, Velquor Pty Ltd.
The company will provide services around the Brintara Skyhold and Tallowbench Suite products.
The company theme is "Work is what you do, not where you go." We aim to separate the concepts of data and place. Our clients can access their data anywhere, any time.
The design should look modern, international and should include the Brintara Associate logo.
Updates
My existing web site is visible at http://quennelworks.example. I am hoping that a good designer can provide a fresh look for the business.
Three images for "Cloud" uploaded today.
Target Market(s)
Business of all kinds
Industry/Entity Type
It Company
Requirements
Nice to have
- Colors and themes might reflect Brintara look and style.

```html
<!DOCTYPE html>
<html lang="en">
<head>
<meta charset="utf-8">
<title>Velquor – Cloud Data Anywhere</title>
<link rel="stylesheet" href="https://fonts.googleapis.com/css2?family=Open+Sans:wght@300;400;600;700&family=Oswald:wght@700&display=swap">
<style>
:root{
  --page:#f8f8f8;
  --white:#ffffff;
  --navy:#2c5a85;
  --navy-dark:#27557f;
  --hero-blue:#3a7cc4;
  --orange:#f0921e;
  --orange-edge:#c9740f;
  --text:#3a3a3a;
  --muted:#6c6c6c;
  --link:#3a6a96;
  --band:#ebebeb;
  --footer:#dadada;
  --rule:#d4d4d4;
}
*{box-sizing:border-box;margin:0;padding:0}
html,body{width:1084px;height:1200px;overflow:hidden}
body{position:relative;background:var(--page);font-family:"Open Sans",Arial,sans-serif;color:var(--text)}
.abs{position:absolute}

.topbar{left:158px;top:0;width:768px;height:46px;background:var(--white);border-bottom:1px solid #eee;font-size:12.5px;color:var(--muted)}
.topbar .contact{position:absolute;right:8px;top:15px;display:flex;gap:12px;align-items:center}
.topbar .phone{color:var(--navy);font-weight:600}
.topbar svg{vertical-align:-2px;margin-right:3px}

.brand{left:162px;top:54px;display:flex;align-items:center;gap:14px}
.brand-mark{width:82px;height:56px;border-radius:50%;background:var(--navy)}
.brand-name{font-size:31px;font-weight:400;color:var(--navy);letter-spacing:1px}

.nav{left:502px;top:72px;display:flex;gap:18px;align-items:center;font-size:12.5px;color:#555}
.nav .active{background:var(--orange);color:var(--white);font-weight:600;padding:4px 9px;border-bottom:2px solid var(--orange-edge)}

.hero{left:158px;top:124px;width:767px;height:299px;border:5px solid var(--navy);background:var(--navy)}
.hero-photo{position:absolute;inset:0;background:linear-gradient(100deg,#c9ccd2 0%,#9fb8d6 28%,#5d6f86 52%,#3a4654 75%,#b98a3e 92%,#d0d4da 100%)}
.hero-panel{position:absolute;left:373px;top:76px;width:389px;height:158px;background:var(--hero-blue);opacity:.96;padding:14px 0 0 29px;color:var(--white)}
.hero-panel h1{font-family:"Oswald",Impact,sans-serif;font-weight:700;font-size:37px;line-height:1.05;letter-spacing:.2px}
.hero-panel p{font-size:17px;font-weight:700;line-height:21px;margin-top:6px}
.btn{display:inline-block;background:var(--orange);color:var(--white);border-bottom:2px solid var(--orange-edge)}
.hero-panel .btn{margin-top:13px;font-size:12px;font-weight:700;padding:3px 14px;color:#3a2a10}

.section-title{font-size:32px;font-weight:400;color:#3a3a3a}
.services-title{left:162px;top:444px}
.service{top:496px;width:220px;text-align:center}
.service .icon{width:75px;height:75px;border-radius:50%;background:var(--navy);margin:0 auto;display:flex;align-items:center;justify-content:center}
.service h3{font-size:16.5px;font-weight:400;margin-top:10px;color:#222}
.service p{font-size:10.5px;color:#777;line-height:13px;margin-top:2px}
.service .btn{font-size:12px;padding:3px 7px;margin-top:7px}
.col-rule{top:504px;width:2px;height:168px;background:linear-gradient(to right,#e6e6e6,#fff)}
.divider{left:294px;top:702px;width:496px;height:1px;background:var(--rule)}

.testimonials-title{left:163px;top:718px}
.testimonial{top:774px;display:flex;gap:8px;width:360px}
.avatar{flex:none;width:82px;height:82px;border-radius:50%;border:3px solid #111;background:linear-gradient(160deg,#cfd6de,#5e6d80)}
.testimonial blockquote{font-size:10.5px;line-height:13px;color:#666;margin-top:6px;max-width:256px}
.testimonial cite{display:block;font-style:normal;font-weight:600;font-size:11.5px;color:#222;margin-top:6px}

.clients{left:0;top:917px;width:1084px;height:49px;background:var(--band);display:flex;justify-content:center;align-items:center;gap:28px;font-size:19px;color:#666}
.clients span{display:flex;align-items:center;gap:6px}
.clients i{display:inline-block;width:14px;height:14px;border-radius:50%;background:#8a8a8a}

.footer{left:0;top:966px;width:1084px;height:191px;background:var(--footer)}
.fcol{top:28px}
.fcol h4{font-size:17px;font-weight:300;color:#333;margin-bottom:9px;letter-spacing:-.3px}
.fcol li{list-style:none;font-size:10.5px;line-height:16.2px;color:var(--link)}
.badge{left:713px;top:128px;width:92px;height:44px;border-radius:4px;background:#c4c8cc}
.social{left:824px;top:135px;display:flex;gap:7px}
.social span{width:26px;height:26px;border-radius:50%;background:var(--white)}

.bottombar{left:0;top:1157px;width:1084px;height:43px;background:var(--navy-dark);color:#dfe7ef;font-size:10px;letter-spacing:-.2px;white-space:nowrap}
.bottombar .copy{position:absolute;left:160px;top:15px}
.bottombar .links{position:absolute;right:159px;top:15px}
</style>
</head>
<body>

<div class="abs topbar">
  <div class="contact">
    <span><svg width="10" height="8" viewBox="0 0 10 8"><rect x=".5" y=".5" width="9" height="7" fill="none" stroke="#3a7cc4"/><path d="M.5 .5L5 4.5 9.5 .5" fill="none" stroke="#3a7cc4"/></svg>service@velquor.example</span>
    <span class="phone"><svg width="6" height="10" viewBox="0 0 6 10"><rect x=".5" y=".5" width="5" height="9" rx="1" fill="none" stroke="#2c5a85"/></svg>08 5550 1274</span>
  </div>
</div>

<div class="abs brand">
  <div class="brand-mark" role="img" aria-label="Velquor mark"></div>
  <div class="brand-name">VELQUOR</div>
</div>

<nav class="abs nav">
  <span class="active">Home</span>
  <span>Remote Backup</span>
  <span>Our Clients</span>
  <span>Testimonials</span>
  <span>About us</span>
</nav>

<section class="abs hero">
  <div class="hero-photo" role="img" aria-label="Technician in a blue sweater working at server racks with orange cabling"></div>
  <div class="hero-panel">
    <h1>Cloud Data Anywhere</h1>
    <p>We help your business and your people work anywhere, any time.</p>
    <span class="btn">Read More</span>
  </div>
</section>

<h2 class="abs section-title services-title">Our Services:-</h2>

<div class="abs service" style="left:150px">
  <div class="icon"><svg width="46" height="32" viewBox="0 0 46 32"><path d="M10 30h27a8 8 0 0 0 1-16 12 12 0 0 0-22-4 9 9 0 0 0-6 20z" fill="#fff"/></svg></div>
  <h3>Brintara Skyhold</h3>
  <p>Quennel Works Computer Services operates secure Backup Servers at our Swanport IX Data Centre.</p>
  <span class="btn">Read More</span>
</div>
<div class="abs col-rule" style="left:401px"></div>
<div class="abs service" style="left:432px">
  <div class="icon"><svg width="28" height="34" viewBox="0 0 28 34"><path d="M7 15V10a7 7 0 0 1 14 0v5" fill="none" stroke="#fff" stroke-width="3.5"/><rect x="2" y="14" width="24" height="19" rx="2" fill="#fff"/><circle cx="14" cy="22" r="2.5" fill="#2c5a85"/><rect x="13" y="23" width="2" height="5" fill="#2c5a85"/></svg></div>
  <h3>Safe ans Secure</h3>
  <p>Cloud Data Anywhere<br>We help your business and your people work anywhere, any time</p>
  <span class="btn">Read More</span>
</div>
<div class="abs col-rule" style="left:684px"></div>
<div class="abs service" style="left:712px">
  <div class="icon"><svg width="40" height="34" viewBox="0 0 40 34" fill="none" stroke="#fff" stroke-width="2.5"><path d="M2 4h6l5 18h20l4-13H10"/><path d="M16 9v13M22 9v13M28 9v13M11 15h24"/><circle cx="15" cy="28" r="2.5"/><circle cx="31" cy="28" r="2.5"/></svg></div>
  <h3>365 products</h3>
  <p>Quennel Works Computer Services operates secure Backup Servers at our Swanport IX Data Centre.</p>
  <span class="btn">See Products</span>
</div>

<div class="abs divider"></div>

<h2 class="abs section-title testimonials-title">Testimonials:-</h2>
<div class="abs testimonial" style="left:166px">
  <div class="avatar" role="img" aria-label="Portrait of Hollis Crane"></div>
  <div>
    <blockquote>"You are a legend. We have an audit in progress today and I was able to illustrate a "Live" recovery. Thank you for service above and beyond the call of duty. We really appreciate that."</blockquote>
    <cite>Hollis Crane, Keystone Ledger</cite>
  </div>
</div>
<div class="abs col-rule" style="left:543px;top:750px;height:135px"></div>
<div class="abs testimonial" style="left:575px">
  <div class="avatar" role="img" aria-label="Portrait of Marcus Tierney"></div>
  <div>
    <blockquote>"You are a legend. We have an audit in progress today and I was able to illustrate a "Live" recovery. Thank you for service above and beyond the call of duty. We really appreciate that."</blockquote>
    <cite>Marcus Tierney, Keystone Ledger</cite>
  </div>
</div>

<div class="abs clients">
  <span><i></i>Harlow</span>
  <span>Upward</span>
  <span>Marisol</span>
  <span>Gearstone</span>
  <span><i></i>Northway</span>
  <span>Greyform</span>
</div>

<footer class="abs footer">
  <div class="abs fcol" style="left:163px"><h4>About Velquor</h4><ul><li>Contact Details</li><li>Catalogue</li><li>Management Team</li><li>Careers</li><li>Mla Guarantee</li><li>Mla Terms Of Business</li></ul></div>
  <div class="abs fcol" style="left:334px"><h4>FAQ</h4><ul><li>Sit Amet Conse Ctetur</li><li>Adipisicing Elit</li><li>Sed Dolor</li><li>Lorem Ipsum Dolor</li><li>Sed Dolor</li><li>Lorem Ipsum Dolor</li></ul></div>
  <div class="abs fcol" style="left:509px"><h4>Links</h4><ul><li>File Sharing</li><li>Document management</li><li>Project management</li><li>Hosted Internet</li><li>Collaboration Online Software</li><li>Online Document Sharing</li></ul></div>
  <div class="abs fcol" style="left:712px"><h4>Contact Us</h4><ul><li>PO Box 418, Riverton</li><li>Western Australia,6999</li><li>Telephone:08 5550 1274</li><li>Email and Support:service@velquor.example</li></ul></div>
  <div class="abs badge" role="img" aria-label="Brintara Associate badge"></div>
  <div class="abs social" aria-label="Social links"><span></span><span></span><span></span></div>
</footer>

<div class="abs bottombar">
  <div class="copy">Copyright © 2013 Quennel Works Computer Services. All Rights Reserved.</div>
  <div class="links">Home | Remote Backup | Emergency Services | Testimonials | Our Clients | About Us</div>
</div>

</body>
</html>
```